plumrivet-loans.com

We are a small dollar lending company that will revolutionize the industry. We will do this by being completely transparent, fee free, etc and an interest rate that normal people can afford to pay. Over 10X less than our competition. We only allow our members to pay bills " bills paid fast", within 72 hours. Payday loans typically charge from 390%-600% with a terrible payback structure. We charge 36%, period, with a payback structure over 12 months. Our site will be very simple and easy to use but elegant at the same time. We do not want the site to be too busy, less is more and easier. We will have; Home, The Story, Why Plumrivet.com, Are you eligible? Members, Clients. To become a member you have to be referred by a current client of Plumrivet.com. A lot of the busy stuff will be saved for the Members and Clients sections. The feel must be elegant, easy to use and very simple to understand. I am looking for the green, white and black combinations of colors, very similar to my logo that was designed by ArtHively.

```html
<!DOCTYPE html>
<html lang="en">
<head>
<meta charset="utf-8">
<title>Plumrivet – Dollar Lending</title>
<link href="https://fonts.googleapis.com/css2?family=Lato:wght@300;400;700&family=Signika:wght@400;600&family=Bebas+Neue&display=swap" rel="stylesheet">
<style>
:root{
  --green:#8dc63f;
  --green-light:#a6d46a;
  --green-dark:#6fa82a;
  --ink:#333333;
  --text:#444444;
  --paper:#efeee9;
  --white:#ffffff;
  --line:#dcdcd6;
}
*{margin:0;padding:0;box-sizing:border-box}
html,body{width:1120px;height:1200px;overflow:hidden}
body{background:var(--paper);font-family:'Lato',sans-serif;color:var(--text);position:relative}
.topbar{position:absolute;left:0;top:0;width:1120px;height:44px;background:var(--ink)}
.call{position:absolute;left:672px;top:13px;font-size:15px;color:var(--green);font-weight:400}
.call b{color:var(--white);font-weight:700}
.social{position:absolute;top:10px;left:834px;display:flex;gap:4px}
.social span{width:25px;height:25px;background:#8a8a8a;display:block}
.header{position:absolute;left:0;top:44px;width:1120px;height:113px;background:var(--paper);border-bottom:1px solid var(--line)}
.brand{position:absolute;left:170px;top:38px;display:flex;align-items:center;gap:10px;font-size:30px;font-weight:400;color:var(--ink)}
.brand i{width:30px;height:30px;border-radius:50%;background:var(--green);display:block}
.nav{position:absolute;left:432px;top:42px;display:flex;align-items:center;font-size:12px;color:var(--ink)}
.nav a{color:inherit;text-decoration:none;padding:0 11px;line-height:31px}
.nav a.active{background:var(--green);color:var(--white);border-radius:2px;padding:0 10px;margin-right:2px}
.hero{position:absolute;left:0;top:157px;width:1120px;height:329px;background:var(--green)}
.hero svg{position:absolute;left:0;top:0}
.card{position:absolute;left:400px;top:264px;width:316px;height:230px;background:var(--green);border:6px solid var(--green-light);border-bottom:none;border-radius:28px 28px 0 0;padding:27px 0 0 34px}
.card li{list-style:none;font-family:'Signika',sans-serif;font-size:19px;color:var(--white);height:32px;display:flex;align-items:center;gap:9px}
.ribbon{position:absolute;left:343px;top:460px}
.ribbon-text{position:absolute;left:378px;top:476px;width:364px;height:54px;background:var(--ink);color:var(--white);font-family:'Bebas Neue',sans-serif;font-size:29px;text-align:center;line-height:58px;letter-spacing:.2px}
.welcome{position:absolute;left:170px;top:590px;width:490px}
.welcome h1{font-size:38px;font-weight:400;color:var(--ink);margin-bottom:14px;margin-left:2px}
.welcome h1 em{font-style:normal;color:var(--green)}
.welcome p{font-size:12.6px;line-height:19.2px;margin-bottom:19px}
.welcome .lead{color:var(--green);font-weight:700;display:block}
.welcome u{text-decoration:underline}
.members{position:absolute;left:691px;top:603px;width:262px;height:307px;background:var(--white);border:1px solid #e3e3de;padding:10px 13px 0 16px}
.members h2{font-size:20px;font-weight:400;color:var(--green);display:flex;align-items:center;gap:7px;padding-bottom:8px;border-bottom:1px solid #ddd;margin-left:-2px}
.members p{font-size:12.6px;line-height:19.2px;margin-top:12px;color:var(--text)}
.members p+p{margin-top:19px}
.members a{display:block;margin-top:8px;color:var(--green);font-weight:700;font-size:12.6px;text-decoration:none}
.cta{position:absolute;left:170px;top:966px;width:781px;height:102px;background:var(--green);border-radius:2px;overflow:hidden}
.cta-art{position:absolute;left:0;top:0;width:230px;height:102px;background:linear-gradient(90deg,var(--green-dark),var(--green))}
.cta h3{position:absolute;left:216px;top:26px;font-size:41px;font-weight:300;color:var(--white);letter-spacing:.5px}
.cta-btn{position:absolute;left:619px;top:28px;width:136px;height:46px;background:var(--green-light);border:2px solid #b5dc80;border-radius:3px;box-shadow:0 3px 0 var(--green-dark);font-size:13px;font-weight:700;color:var(--ink);text-align:center;line-height:42px}
.footer{position:absolute;left:0;top:1128px;width:1120px;height:72px;background:var(--ink);text-align:center}
.footer nav{margin-top:18px;font-size:11.5px;color:var(--white);font-weight:400}
.footer nav span{color:#999;margin:0 4px}
.footer small{display:block;margin-top:6px;font-size:11px;color:#bbb}
</style>
</head>
<body>
<div class="topbar">
  <div class="call">CALL US <b>555.014.2290</b></div>
  <div class="social" aria-label="Social links"><span></span><span></span><span></span><span></span></div>
</div>

<header class="header">
  <div class="brand"><i></i>Plumrivet</div>
  <nav class="nav">
    <a class="active">Home</a><a>The Story</a><a>Why Plumrivet.com</a><a>Are you eligible?</a><a>Members</a><a>Clients</a><a>Contact</a>
  </nav>
</header>

<section class="hero">
  <svg width="1120" height="329" viewBox="0 0 1120 329">
    <path role="img" aria-label="Fan of dollar banknotes spread in a half circle" d="M165 329 A395 290 0 0 1 955 329 Z" fill="#a2cf63"/>
  </svg>
</section>

<div class="card">
  <ul>
    <li><svg width="20" height="18" viewBox="0 0 20 18"><path d="M2 9 L8 15 L18 2" fill="none" stroke="#fff" stroke-width="3.4"/></svg>Completely Transparent</li>
    <li><svg width="20" height="18" viewBox="0 0 20 18"><path d="M2 9 L8 15 L18 2" fill="none" stroke="#fff" stroke-width="3.4"/></svg>Fee Free Service</li>
    <li><svg width="20" height="18" viewBox="0 0 20 18"><path d="M2 9 L8 15 L18 2" fill="none" stroke="#fff" stroke-width="3.4"/></svg>Affordable Interest Rate</li>
    <li><svg width="20" height="18" viewBox="0 0 20 18"><path d="M2 9 L8 15 L18 2" fill="none" stroke="#fff" stroke-width="3.4"/></svg>Pay Bills within 72 hours &amp;</li>
    <li><svg width="20" height="18" viewBox="0 0 20 18"><path d="M2 9 L8 15 L18 2" fill="none" stroke="#fff" stroke-width="3.4"/></svg>Much more</li>
  </ul>
</div>

<svg class="ribbon" width="434" height="48" viewBox="0 0 434 48">
  <path d="M17 0 H57 V45 H0 Z" fill="#222"/>
  <path d="M417 0 H377 V45 H434 Z" fill="#222"/>
</svg>
<div class="ribbon-text">WE ARE A DOLLAR LENDING COMPANY</div>

<main class="welcome">
  <h1>Welcome to <em>Plumrivet</em></h1>
  <p><span class="lead">Lorem ipsum dolor sit amet, consectetur adipiscing elit.</span>Sed quis nisi euismod, fermentum tellus a, lobortis quam. Vestibulum condimentum mi vitae diam tristique, egestas dignissim diam mattis. <b>Curabitur vel diam</b> in massa porttitor dictum id in lorem. Vivamus faucibus ac leo ac dignissim.</p>
  <p>Maecenas orci est, euismod facilisis feugiat sit amet, semper ut tortor. Donec eleifend accumsan nisl, nec laoreet leo iaculis sit amet. Vivamus eu <u>magna rhoncus</u>, consectetur metus ac, varius lacus. Donec ultricies, tortor quis sagittis sagittis, mauris erat ullamcorper augue, eu placerat diam nunc a lorem.</p>
  <p><span class="lead">Nam vulputate mauris id arcu pharetra</span>Nullam eget massa vel mi posuere venenatis sed quis tortor. In hac habitasse platea dictumst. Fusce nisi tellus, fermentum a luctus eget, convallis vitae orci. In commodo egestas magna quis placerat.</p>
</main>

<aside class="members">
  <h2><svg width="28" height="20" viewBox="0 0 28 20"><circle cx="9" cy="6" r="5" fill="#aaa"/><circle cx="19" cy="5" r="4.5" fill="#aaa"/><path d="M0 20 Q9 8 18 20Z" fill="#aaa"/><path d="M12 17 Q19 6 28 17Z" fill="#aaa"/></svg>MEMBERS</h2>
  <p>Aenean posuere velit a erat placerat, id euismod magna rutrum. Curabitur ac sollicitudin tellus. Aenean gravida nisl ut ligula facilisis, sed sollicitudin ipsum hendrerit.</p>
  <p>Vestibulum lacinia congue commodo. Sed lorem erat, euismod at risus at, sollicitudin venenatis risus. Praesent cursus lacus ac eros feugiat, vitae eleifend felis hendrerit.</p>
  <a>Know More&gt;</a>
</aside>

<section class="cta">
  <div class="cta-art" role="img" aria-label="Illustration of raised thumbs-up hands with swirl ornaments"></div>
  <h3>ARE YOU ELIGIBLE?</h3>
  <div class="cta-btn">DISCOVER NOW</div>
</section>

<footer class="footer">
  <nav>HOME<span>/</span>THE STORY<span>/</span>WHY PLUMRIVET.COM<span>/</span>ARE YOU ELIGIBLE?<span>/</span>MEMBERS<span>/</span>CLIENTS<span>/</span>CONTACT US</nav>
  <small>Copyright © 2014 plumrivet-loans.com. All rights reserved.</small>
</footer>
</body>
</html>
```